Law Firm Redesign of Stationery

We are a law firm that just expanded to our second location. We had a redesign on our logo for signage and we are now looking for a redesign of business cards (updated for our 6 current staff), letterhead, and envelopes for the new logo and include both locations. We have the Illustrator file for the new logo and the Illustrator or EPS files for all previous stationery. We would like to keep the same blue/gray color scheme but try and find a new look that matches the new logo. Our locations are in the Baltimore/D.C. metro area so something fresh, professional, and urban is the direction we would like to go in.
Industry/Entity Type
Legal
Contact Information for Business Card
See attached AI or EPS files for current business card designs
Requirements
Must have
- Must have both office addresses included: 514 Tessel Hwy, N.W., Brindle Harbor, MD 21190 and 4183 Ferndusk Way, Elkmont, MD 21098. We would like to maintain the current blue and grey color scheme.

```html
<!DOCTYPE html>
<html lang="en">
<head>
<meta charset="utf-8">
<title>Harlow &amp; Co. Chtd — Stationery</title>
<link href="https://fonts.googleapis.com/css2?family=Lato:wght@400;700&display=swap" rel="stylesheet">
<style>
  :root {
    --brand-blue: #3a6fb8;
    --brand-blue-deep: #2f5fa8;
    --brand-grey: #8a8b8d;
    --paper: #f6f6f6;
    --backdrop: #dcdcdc;
    --ink-grey: #6d6f72;
    --white: #ffffff;
  }
  * { box-sizing: border-box; margin: 0; padding: 0; }
  html, body { width: 1200px; height: 668px; overflow: hidden; }
  body {
    background: var(--backdrop);
    font-family: "Lato", Arial, sans-serif;
    position: relative;
  }

  /* Letterhead */
  .letterhead {
    position: absolute; left: 70px; top: 52px; width: 388px; height: 549px;
    background: var(--paper);
  }
  .letterhead__top-rule { position: absolute; left: 0; top: 0; width: 100%; height: 8px; background: var(--brand-grey); }
  .letterhead__tab { position: absolute; left: 97px; top: 0; width: 194px; height: 16px; }
  .letterhead__mark-bg {
    position: absolute; left: 130px; top: 210px; width: 132px; height: 126px;
    border: 4px solid #e9e9e9; background: #eeeeee;
  }
  .letterhead__base-rule { position: absolute; left: 0; top: 481px; width: 100%; height: 7px; background: var(--brand-grey); }
  .letterhead__footer {
    position: absolute; left: 0; top: 494px; width: 100%; height: 55px;
    background: var(--brand-blue-deep); color: var(--white);
    font-size: 7px; line-height: 13px;
  }
  .contact { position: absolute; display: flex; gap: 5px; align-items: flex-start; white-space: nowrap; }
  .contact svg { width: 12px; height: 12px; flex: none; margin-top: 1px; }
  .contact--address { left: 8px; top: 14px; }
  .contact--phone { left: 185px; top: 13px; }
  .contact--fax { left: 185px; top: 28px; }
  .contact--email { left: 274px; top: 11px; }
  .contact--web { left: 274px; top: 26px; }

  /* Brand lockup */
  .lockup { position: absolute; text-align: center; }
  .lockup__square { display: block; margin: 0 auto; border: 2px solid var(--brand-blue); background: var(--brand-blue); }
  .lockup__name {
    display: block; font-weight: 400; letter-spacing: 0.04em; white-space: nowrap;
    color: var(--brand-blue);
  }
  .lockup__tagline { display: block; color: var(--ink-grey); letter-spacing: 0.02em; white-space: nowrap; }

  .letterhead .lockup { left: 0; width: 100%; top: 21px; }
  .letterhead .lockup__square { width: 38px; height: 37px; }
  .letterhead .lockup__name { font-size: 20px; margin-top: 4px; }
  .letterhead .lockup__tagline { font-size: 6.5px; margin-top: 1px; }

  /* Envelope */
  .envelope { position: absolute; left: 521px; top: 93px; width: 423px; height: 299px; }
  .envelope svg.envelope__flaps { position: absolute; inset: 0; }
  .envelope .lockup { left: 0; width: 100%; top: 30px; }
  .envelope .lockup__square { width: 44px; height: 42px; }
  .envelope .lockup__name { font-size: 21px; margin-top: 5px; }
  .envelope .lockup__tagline { font-size: 7px; margin-top: 1px; }
  .envelope__web {
    position: absolute; left: 117px; top: 244px; font-size: 8px;
    letter-spacing: 0.5em; color: var(--brand-blue);
  }

  /* Card */
  .card {
    position: absolute; left: 727px; top: 297px; width: 427px; height: 303px;
    background: linear-gradient(135deg, #3f7bc2, #3568b0);
  }
  .card .lockup { left: 0; width: 100%; top: 95px; }
  .card .lockup__square { width: 68px; height: 64px; border-color: var(--white); background: transparent; outline: 2px solid var(--white); outline-offset: -6px; }
  .card .lockup__name { color: var(--white); font-size: 29px; margin-top: 8px; }
  .card .lockup__tagline { color: var(--white); font-size: 10px; margin-top: 2px; }
</style>
</head>
<body>

<section class="letterhead">
  <div class="letterhead__top-rule"></div>
  <svg class="letterhead__tab" viewBox="0 0 194 16"><polygon points="0,0 194,0 181,16 13,16" fill="#3268b2"/></svg>
  <div class="lockup">
    <span class="lockup__square"></span>
    <span class="lockup__name">HARLOW &amp; CO. CHTD</span>
    <span class="lockup__tagline">CITY CALIBER COUNSEL - CLOSE TO HOME CARE</span>
  </div>
  <div class="letterhead__mark-bg"></div>
  <div class="letterhead__base-rule"></div>
  <footer class="letterhead__footer">
    <div class="contact contact--address">
      <svg viewBox="0 0 12 12"><circle cx="6" cy="6" r="5.3" fill="none" stroke="#fff" stroke-width="0.9"/><path d="M6 2.8a2 2 0 0 1 2 2c0 1.5-2 4-2 4s-2-2.5-2-4a2 2 0 0 1 2-2z" fill="#fff"/><circle cx="6" cy="4.8" r="0.7" fill="#2f5fa8"/></svg>
      <div>514 Tessel Hwy, N.W., Brindle Harbor, MD 21190<br>4183 Ferndusk Way, Elkmont, MD 21098</div>
    </div>
    <div class="contact contact--phone">
      <svg viewBox="0 0 12 12"><circle cx="6" cy="6" r="5.3" fill="none" stroke="#fff" stroke-width="0.9"/><path d="M4 3.2l1 1.3-.6.8a4 4 0 0 0 2.3 2.3l.8-.6 1.3 1-.6 1A5 5 0 0 1 3 4z" fill="#fff"/></svg>
      <div>410 - 555 - 0147</div>
    </div>
    <div class="contact contact--fax">
      <svg viewBox="0 0 12 12"><circle cx="6" cy="6" r="5.3" fill="none" stroke="#fff" stroke-width="0.9"/><rect x="3.3" y="5" width="5.4" height="3.4" fill="#fff"/><rect x="4.3" y="3.2" width="3.4" height="1.6" fill="#fff"/></svg>
      <div>410 - 555 - 0182</div>
    </div>
    <div class="contact contact--email">
      <svg viewBox="0 0 12 12"><circle cx="6" cy="6" r="5.3" fill="none" stroke="#fff" stroke-width="0.9"/><rect x="3.2" y="4" width="5.6" height="4" fill="#fff"/><path d="M3.2 4l2.8 2.2L8.8 4" fill="none" stroke="#2f5fa8" stroke-width="0.6"/></svg>
      <div>mbreyer@harlowcochtd.com</div>
    </div>
    <div class="contact contact--web">
      <svg viewBox="0 0 12 12"><circle cx="6" cy="6" r="5.3" fill="none" stroke="#fff" stroke-width="0.9"/><circle cx="6" cy="6" r="3" fill="none" stroke="#fff" stroke-width="0.6"/><ellipse cx="6" cy="6" rx="1.2" ry="3" fill="none" stroke="#fff" stroke-width="0.6"/><line x1="3" y1="6" x2="9" y2="6" stroke="#fff" stroke-width="0.6"/></svg>
      <div>www.harlowcochtd.com</div>
    </div>
  </footer>
</section>

<section class="envelope">
  <svg class="envelope__flaps" viewBox="0 0 423 299" preserveAspectRatio="none">
    <rect width="423" height="299" fill="#f7f7f7"/>
    <polygon points="0,0 130,149 0,270" fill="#3d74bd"/>
    <polygon points="423,0 423,299 307,299 291,150" fill="#3e78bf"/>
    <polygon points="0,0 423,0 204,212" fill="#fafafa"/>
    <polyline points="0,0 204,212 423,0" fill="none" stroke="#e2e2e2" stroke-width="1"/>
  </svg>
  <div class="lockup">
    <span class="lockup__square"></span>
    <span class="lockup__name">HARLOW &amp; CO. CHTD</span>
    <span class="lockup__tagline">CITY CALIBER COUNSEL - CLOSE TO HOME CARE</span>
  </div>
  <div class="envelope__web">WWW.HARLOW</div>
</section>

<section class="card">
  <div class="lockup">
    <span class="lockup__square"></span>
    <span class="lockup__name">HARLOW &amp; CO. CHTD</span>
    <span class="lockup__tagline">CITY CALIBER COUNSEL - CLOSE TO HOME CARE</span>
  </div>
</section>

</body>
</html>
```